Designer Instructions – Updated Referral Program Flyer

(Based on the mock-up in “Brief Layout and Instructions.pdf”)

OVERALL STYLE + LAYOUT

Maintain the same general layout, structure, and flow as the mock-up flyer (front and back).

This is an update of an older flyer, not a full redesign — keep the same sections, proportions, and overall visual feel, but with cleaner, more modern design improvements.

The final flyer should look clean, bold, professional, and high-impact, geared toward realtors, property managers, and contractors who refer work.

FRONT SIDE INSTRUCTIONS
1. Header Section

Remove the Tallow Ridge Builders logo from the top banner.
(Shown on page 1 of the PDF)

2. Main Headline

Keep the same three-line structure:
EARN
UNLIMITED
CASH

Center it, maximize impact, and increase the font size of CASH so all three words match in importance.

Make the headline bold, clean, and the main focal point.

3. Cash Incentive Box

Keep the "$500 minimum OR 10% per referral" box, but upgrade the graphics to look sharper and more modern.

Ensure the wording matches exactly what’s in the mock-up.

4. Premier Partner Program Ribbon

Clean up and modernize the "PREMIER PARTNER PROGRAM" bar while keeping the same position and structure.

Ensure the checkmark badge remains crisp and professional.

5. Supporting Icons Section

Keep the four icons/benefit boxes (Guaranteed Payout, Free Evaluations, Affordable Solutions, Industry Leaders) in the same order.

Update the icons to cleaner, more modern styles — but maintain the same meanings.

Improve alignment and spacing for sharper visual consistency.

6. Remove Icons in Contact Area

At the bottom (“CALL TEXT OR BOOK ONLINE 555-014-2796 TallowRidgeBuilders.example”), remove the phone and internet icons, as noted on page 2 of the PDF.

7. Replace All Images

I (Darnell) will provide all updated stock images separately via email.

Replace the flood/water-damage imagery and roof leak with the new images I send.

Keep image placement and proportions the same as the mock-up.

BACK SIDE INSTRUCTIONS
1. Header Image + “REFER / EARN” Section

Maintain the same large split-image layout (“The more you refer, the more you earn”).

Replace all background imagery with the new assets I will send.

Keep the CASH FLOW image section but modernize the type and spacing.

2. “HOW IT WORKS” Section

Preserve the three-column layout:

Refer Flood, Water & Mold Damage

We Take Care of Everything (evaluations/insurance)

Get Paid to Share

Update images, tighten spacing, and use modern iconography.

3. Remove Phone/Internet Icons

Same as the front side — remove small communication icons and keep only the text/number/URL.

4. Bottom Contact Bar

Keep the blue bar, same wording, same layout — just modernize the style if needed for clarity.

5. Replace All Back-Side Images

Again, I will email you the image assets.

Keep the layout EXACT — just update with higher-quality photos and improved design.

TEXT CONTENT (Keep as-is unless spacing adjustments needed)

All text shown in the PDF should remain exactly the same unless spacing or visual balance requires minor adjustments.
Example from page 3:

“REFER FLOOD, MOLD & CONSTRUCTION JOBS”

“We Schedule a Free Estimate. If Approved, You Get Paid.”

“Everybody Benefits From Referrals”

Everything stays, just refreshed and visually improved.

DESIGN GOALS

Flyer should look high-end and trustworthy, not salesy.

Consistent color theme: blues, whites, yellows, same palette as original.

Use bold, modern fonts with strong readability.

Ensure all headlines pop and all benefit boxes are clean, well-aligned, and evenly spaced.

The final result should feel like a premium referral program flyer for a top-tier restoration/remodel company.

FILES I WILL PROVIDE

I will send the designer:

All replacement stock photos

Any updated logos (if needed)

Original high-resolution version of the mock-up (if available)

Any additional icons preferred

0054AA
0677BA
7BADD7
CADEEF
E8F1F8

• Designer Instructions – Updated Referral Program Flyer (Based on the mock-up in “Brief Layout and Instructions.pdf”) OVERALL STYLE + LAYOUT Maintain the same general layout, structure, and flow as the mock-up flyer (front and back). This is an update of an older flyer, not a full redesign — keep the same sections, proportions, and overall visual feel, but with cleaner, more modern design improvements. The final flyer should look clean, bold, professional, and high-impact, geared toward realtors, property managers, and contractors who refer work. FRONT SIDE INSTRUCTIONS 1. Header Section Remove the Tallow Ridge Builders logo from the top banner. (Shown on page 1 of the PDF) 2. Main Headline Keep the same three-line structure: EARN UNLIMITED CASH Center it, maximize impact, and increase the font size of CASH so all three words match in importance. Make the headline bold, clean, and the main focal point. 3. Cash Incentive Box Keep the "$500 minimum OR 10% per referral" box, but upgrade the graphics to look sharper and more modern. Ensure the wording matches exactly what’s in the mock-up. 4. Premier Partner Program Ribbon Clean up and modernize the "PREMIER PARTNER PROGRAM" bar while keeping the same position and structure. Ensure the checkmark badge remains crisp and professional. 5. Supporting Icons Section Keep the four icons/benefit boxes (Guaranteed Payout, Free Evaluations, Affordable Solutions, Industry Leaders) in the same order. Update the icons to cleaner, more modern styles — but maintain the same meanings. Improve alignment and spacing for sharper visual consistency. 6. Remove Icons in Contact Area At the bottom (“CALL TEXT OR BOOK ONLINE 555-014-2796 TallowRidgeBuilders.example”), remove the phone and internet icons, as noted on page 2 of the PDF. 7. Replace All Images I (Darnell) will provide all updated stock images separately via email. Replace the flood/water-damage imagery and roof leak with the new images I send. Keep image placement and proportions the same as the mock-up. BACK SIDE INSTRUCTIONS 1. Header Image + “REFER / EARN” Section Maintain the same large split-image layout (“The more you refer, the more you earn”). Replace all background imagery with the new assets I will send. Keep the CASH FLOW image section but modernize the type and spacing. 2. “HOW IT WORKS” Section Preserve the three-column layout: Refer Flood, Water & Mold Damage We Take Care of Everything (evaluations/insurance) Get Paid to Share Update images, tighten spacing, and use modern iconography. 3. Remove Phone/Internet Icons Same as the front side — remove small communication icons and keep only the text/number/URL. 4. Bottom Contact Bar Keep the blue bar, same wording, same layout — just modernize the style if needed for clarity. 5. Replace All Back-Side Images Again, I will email you the image assets. Keep the layout EXACT — just update with higher-quality photos and improved design. TEXT CONTENT (Keep as-is unless spacing adjustments needed) All text shown in the PDF should remain exactly the same unless spacing or visual balance requires minor adjustments. Example from page 3: “REFER FLOOD, MOLD & CONSTRUCTION JOBS” “We Schedule a Free Estimate. If Approved, You Get Paid.” “Everybody Benefits From Referrals” Everything stays, just refreshed and visually improved. DESIGN GOALS Flyer should look high-end and trustworthy, not salesy. Consistent color theme: blues, whites, yellows, same palette as original. Use bold, modern fonts with strong readability. Ensure all headlines pop and all benefit boxes are clean, well-aligned, and evenly spaced. The final result should feel like a premium referral program flyer for a top-tier restoration/remodel company. FILES I WILL PROVIDE I will send the designer: All replacement stock photos Any updated logos (if needed) Original high-resolution version of the mock-up (if available) Any additional icons preferred

```html
<!DOCTYPE html>
<html lang="en">
<head>
<meta charset="utf-8">
<title>Tallow Ridge Builders – Referral Program Flyer</title>
<link href="https://fonts.googleapis.com/css2?family=Montserrat:wght@400;500;600;700;800;900&family=Anton&display=swap" rel="stylesheet">
<style>
  :root{
    --blue:#1753ab;
    --blue-deep:#0d3f8c;
    --navy:#0e1824;
    --red:#e8232a;
    --yellow:#f4e92b;
    --orange:#f59a1e;
    --sky:#cadeef;
    --ice:#e8f1f8;
    --ink:#151515;
    --white:#ffffff;
  }
  *{box-sizing:border-box;margin:0;padding:0}
  html,body{width:800px;height:1200px;overflow:hidden;background:var(--white)}
  body{position:relative;font-family:"Montserrat",Arial,sans-serif;color:var(--ink)}
  .flyer{position:absolute;left:46px;width:708px;height:457px;background:var(--white);overflow:hidden}
  .flyer--front{top:44px}
  .flyer--back{top:543px}
  .flyer svg.backdrop{position:absolute;left:0;top:0;width:708px;height:457px}
  .abs{position:absolute}

  /* front headline */
  .headline{left:0;top:0;width:370px;height:140px;font-weight:900;color:var(--white)}
  .headline span{position:absolute;left:0;width:370px;text-align:center;line-height:1;letter-spacing:-1px;white-space:nowrap}
  .headline .earn{top:11px;color:var(--yellow);font-size:52px}
  .headline .unlimited{top:56px;font-size:40px}
  .headline .cash{top:88px;font-size:54px}
  .tagline{left:34px;top:145px;font-weight:800;font-size:19px;color:var(--blue);letter-spacing:.2px}

  .offer-min{left:22px;top:188px;color:var(--white);font-weight:800;line-height:1}
  .offer-min .amount{font-size:20px}
  .offer-min .amount sup{font-size:10px;vertical-align:8px}
  .offer-min .label{display:block;font-size:12px;font-weight:600;letter-spacing:.5px;margin-top:2px}
  .offer-or{left:142px;top:193px;font-size:19px;font-weight:800;color:var(--blue)}
  .offer-pct{left:192px;top:186px;color:var(--white);font-size:35px;font-weight:500;line-height:1.15}
  .offer-per{left:266px;top:192px;color:var(--white);font-size:13px;font-weight:600;line-height:1.05;letter-spacing:.3px}

  .premier{left:384px;width:324px;top:187px;text-align:center;font-size:10.5px;font-weight:500;letter-spacing:9px;color:var(--blue);padding-left:6px}
  .ribbon-word{top:207px;font-size:14px;font-weight:800;color:var(--white);text-align:center}
  .ribbon-partner{left:400px;width:156px}
  .ribbon-program{left:572px;width:136px}

  .section-title{left:0;width:708px;text-align:center;font-weight:800;color:var(--blue)}
  .section-title em{font-style:normal;color:var(--red)}
  .wins{top:240px;font-size:20.5px}
  .grow{top:381px;font-size:20.5px}

  .benefit{top:280px;width:140px;height:92px}
  .benefit .tab{position:absolute;left:0;top:0;width:116px;height:37px;border:3px solid var(--blue);border-radius:18px;background:var(--white);text-align:center;font-size:11px;font-weight:700;line-height:1.08;color:var(--blue);padding-top:4px;z-index:2}
  .benefit .frame{position:absolute;left:0;top:18px;width:119px;height:71px;border-left:1.5px solid var(--blue);border-bottom:1.5px solid var(--blue);border-bottom-left-radius:8px}
  .benefit .frame::after{content:"";position:absolute;right:-3px;bottom:-3.5px;width:5px;height:5px;border-radius:50%;background:var(--blue)}
  .benefit p{position:absolute;left:5px;top:41px;font-size:10px;line-height:12.5px;color:var(--ink);white-space:nowrap}
  .benefit svg{position:absolute;left:101px;top:42px;width:38px;height:38px;fill:none;stroke:#5b86c4;stroke-width:1.4;stroke-linecap:round;stroke-linejoin:round}

  .contact-cta{left:22px;top:421px;font-size:16px;font-weight:800;color:var(--white);letter-spacing:.2px}
  .contact-cta .hi{color:var(--yellow)}
  .contact-cta .thin{font-weight:400}
  .contact-line{left:306px;top:423px;font-size:14.5px;font-weight:700;color:var(--ink)}

  /* back */
  .slogan{left:89px;top:0;width:134px;height:180px;font-family:"Anton",Impact,sans-serif;font-weight:400;color:var(--white)}
  .slogan span{position:absolute;left:0;width:134px;text-align:center;line-height:1;white-space:nowrap}
  .slogan .small{font-size:25px}
  .slogan .big{font-size:64px;color:#f7c21c;background:linear-gradient(180deg,var(--yellow) 15%,#f7c51c 55%,var(--orange) 90%);-webkit-background-clip:text;background-clip:text;-webkit-text-fill-color:transparent}
  .slogan .l1{top:15px}
  .slogan .l2{top:32px}
  .slogan .l3{top:89px}
  .slogan .l4{top:108px}
  .how{left:22px;top:189px;font-size:23px;font-weight:900;color:var(--blue)}
  .cashflow{left:371px;top:101px;font-size:37px;font-weight:900;letter-spacing:-1px;line-height:1;color:var(--blue-deep);white-space:nowrap}
  .cashflow em{font-style:normal;color:var(--red)}

  .step{top:227px;width:185px;height:158px;border:1.5px solid var(--blue);border-radius:10px;overflow:hidden;text-align:center}
  .step .photo{height:87px}
  .step h3{font-size:11.5px;font-weight:800;color:var(--blue);line-height:1.12;margin-top:8px}
  .step p{font-size:10.5px;line-height:1.22;margin-top:5px;color:var(--ink)}
  .refer-list{top:391px;font-size:18px}
</style>
</head>
<body>

<!-- FRONT -->
<section class="flyer flyer--front" aria-label="Referral program flyer, front">
  <svg class="backdrop" viewBox="0 0 708 457">
    <defs>
      <linearGradient id="headerBlue" x1="0" y1="0" x2="1" y2="1">
        <stop offset="0" stop-color="#1b5bb4"/><stop offset="1" stop-color="#1650a5"/>
      </linearGradient>
      <linearGradient id="dryingPhoto" x1="0" y1="0" x2="0" y2="1">
        <stop offset="0" stop-color="#d9d6d1"/><stop offset=".55" stop-color="#8fb9d3"/><stop offset="1" stop-color="#c9c7c4"/>
      </linearGradient>
    </defs>
    <rect class="header-band" x="0" y="0" width="708" height="181" fill="url(#headerBlue)"/>
    <g role="img" aria-label="City skyline faintly behind the headline">
      <rect x="40" y="70" width="300" height="95" fill="#2a66bd" opacity=".35"/>
    </g>
    <g role="img" aria-label="Photo of blue air movers and dehumidifiers drying a flooded room">
      <polygon points="380,0 708,0 708,181 384,181 338,88" fill="url(#dryingPhoto)" stroke="#fff" stroke-width="3"/>
    </g>
    <polygon class="tagline-strip" points="22,143 380,143 392,172 22,172" fill="var(--yellow)"/>

    <polygon class="offer-min-shape" points="0,185 122,185 136,206.5 122,228 0,228" fill="var(--red)"/>
    <polygon class="offer-pct-shape" points="176,185 382,185 364,228 176,228 164,206.5" fill="var(--red)"/>

    <rect class="premier-band" x="384" y="185" width="324" height="18" fill="var(--sky)"/>
    <polygon class="ribbon-red" points="392,203 560,203 560,228 402,228" fill="var(--red)"/>
    <rect class="ribbon-blue" x="560" y="203" width="148" height="25" fill="var(--blue)"/>
    <path class="ribbon-shield" d="M545 201 L573 201 L573 214 Q573 226 559 232 Q545 226 545 214 Z" fill="#fff"/>
    <path class="ribbon-check" d="M552 215 L557 221 L566 206" fill="none" stroke="var(--blue)" stroke-width="2.5" stroke-linecap="round" stroke-linejoin="round"/>

    <polygon class="contact-bar" points="0,416 288,416 300,444 0,444" fill="var(--blue)"/>
  </svg>

  <h1 class="abs headline"><span class="earn">EARN</span><span class="unlimited">UNLIMITED</span><span class="cash">CASH</span></h1>
  <div class="abs tagline">GET PAID TO REFER A FLOOD</div>

  <div class="abs offer-min"><span class="amount"><sup>$</sup>500</span><span class="label">MINIMUM</span></div>
  <div class="abs offer-or">or</div>
  <div class="abs offer-pct">10%</div>
  <div class="abs offer-per">PER<br>REFERRAL</div>

  <div class="abs premier">PREMIER</div>
  <div class="abs ribbon-word ribbon-partner">PARTNER</div>
  <div class="abs ribbon-word ribbon-program">PROGRAM</div>

  <h2 class="abs section-title wins">PARTNER WITH US &amp; <em>EVERYBODY WINS!</em></h2>

  <div class="abs benefit" style="left:22px">
    <div class="tab">Guaranteed<br>Payout</div><div class="frame"></div>
    <p>Minimum $500<br>or 10% of Total<br>Invoice Paid Fast</p>
    <svg viewBox="0 0 38 38"><rect x="2" y="2" width="32" height="20" rx="2"/><circle cx="18" cy="12" r="3"/><path d="M7 12h4M25 12h4M18 36V20M13 25l5-5 5 5"/></svg>
  </div>
  <div class="abs benefit" style="left:195px">
    <div class="tab">Free<br>Evaluations</div><div class="frame"></div>
    <p>Fast &amp; Free<br>Inspections &amp;<br>Written Estimates</p>
    <svg viewBox="0 0 38 38"><rect x="3" y="3" width="24" height="32" rx="2"/><path d="M8 11l2 2 3-4M16 11h7M8 19l2 2 3-4M16 19h7M8 27l4 4M12 27l-4 4M16 29h7"/><rect x="31" y="6" width="4" height="24" rx="1"/></svg>
  </div>
  <div class="abs benefit" style="left:371px">
    <div class="tab">Affordable<br>Solutions</div><div class="frame"></div>
    <p>Lowest Out of<br>Pocket Costs for<br>Your Customers</p>
    <svg viewBox="0 0 38 38"><rect x="16" y="2" width="18" height="16" rx="2"/><path d="M27 6h-4a2 2 0 000 4h2a2 2 0 010 4h-4M25 4v2M25 14v2"/><path d="M2 26l6-4h8l6 2h-8M8 34l4-2h12l10-8-2-2-8 5"/></svg>
  </div>
  <div class="abs benefit" style="left:543px">
    <div class="tab">Industry<br>Leaders</div><div class="frame"></div>
    <p>Licensed &amp; Certified<br>Experts Provide<br>100% Guarante</p>
    <svg viewBox="0 0 38 38"><circle cx="19" cy="6" r="4"/><path d="M11 20a8 8 0 0116 0"/><path d="M2 24h34l-4 5 4 5H2l4-5z"/><circle cx="19" cy="28" r="6"/><path d="M19 24.5l1 2.2 2.3.2-1.8 1.5.6 2.3-2.1-1.3-2.1 1.3.6-2.3-1.8-1.5 2.3-.2z"/></svg>
  </div>

  <h2 class="abs section-title grow">SEND <em>REFERRALS.</em> GET <em>PAID.</em> GROW YOUR <em>BUSINESS.</em></h2>

  <div class="abs contact-cta">CALL <span class="hi">TEXT</span> <span class="thin">OR</span> BOOK <span class="hi">ONLINE</span></div>
  <div class="abs contact-line">555-014-2796 | www.TallowRidgeBuilders.example</div>
</section>

<!-- BACK -->
<section class="flyer flyer--back" aria-label="Referral program flyer, back">
  <svg class="backdrop" viewBox="0 0 708 457">
    <defs>
      <linearGradient id="leftPhoto" x1="0" y1="0" x2="1" y2="0">
        <stop offset="0" stop-color="#2a5fa8"/><stop offset="1" stop-color="#1650a5"/>
      </linearGradient>
      <linearGradient id="cashPhoto" x1="0" y1="0" x2="1" y2="1">
        <stop offset="0" stop-color="#e6e6e2"/><stop offset=".5" stop-color="#b9bdb8"/><stop offset="1" stop-color="#dcdcd7"/>
      </linearGradient>
      <linearGradient id="curl" x1="0" y1="0" x2="1" y2="0">
        <stop offset="0" stop-color="#0d3f8c"/><stop offset=".5" stop-color="#2a6ed0"/><stop offset="1" stop-color="#0b3578"/>
      </linearGradient>
    </defs>
    <g role="img" aria-label="Photo of a technician with water damage equipment, tinted blue">
      <rect x="0" y="0" width="380" height="199" fill="url(#leftPhoto)"/>
    </g>
    <polygon class="dark-panel" points="120,42 238,42 372,199 120,199" fill="var(--navy)"/>
    <g role="img" aria-label="Photo of scattered hundred dollar bills">
      <polygon points="322,0 708,0 708,199 372,199 346,95" fill="url(#cashPhoto)" stroke="#fff" stroke-width="3"/>
    </g>
    <path class="cashflow-strip" d="M350 78 L632 74 L632 154 L352 152 L356 140 L350 128 L355 116 L349 104 L354 92 Z" fill="var(--sky)"/>
    <path class="cashflow-curl" d="M630 62 Q648 54 666 62 L666 154 Q648 146 630 158 Z" fill="url(#curl)"/>
    <polygon class="how-strip" points="0,188 242,188 254,217 0,217" fill="var(--yellow)"/>
    <polygon class="contact-bar" points="0,416 288,416 300,444 0,444" fill="var(--blue)"/>
  </svg>

  <h1 class="abs slogan"><span class="small l1">THE MORE YOU</span><span class="big l2">REFER</span><span class="small l3">THE MORE YOU</span><span class="big l4">EARN</span></h1>
  <div class="abs cashflow">CASH <em>FLOW</em></div>
  <h2 class="abs how">HOW IT WORKS</h2>

  <article class="abs step" style="left:23px">
    <div class="photo" role="img" aria-label="Photo of a city skyline at dusk over the bay" style="background:linear-gradient(180deg,#8d7fa6 0%,#c99a8f 55%,#3d4a74 100%)"></div>
    <h3>REFER FLOOD, MOLD<br>&amp; CONSTRUCTION JOBS</h3>
    <p>It’s Simple to Refer 24/7:<br>Call, Text or Book Online.</p>
  </article>
  <article class="abs step" style="left:261px">
    <div class="photo" role="img" aria-label="Photo of an inspector holding a work estimate outside a house" style="background:linear-gradient(180deg,#9aa88a 0%,#c9c6bf 50%,#6f9a4f 100%)"></div>
    <h3>WE TAKE CARE OF<br>EVERYTHING</h3>
    <p>We Schedule a Free Estimate.<br>If Approved, You Get Paid.</p>
  </article>
  <article class="abs step" style="left:498px">
    <div class="photo" role="img" aria-label="Photo of a yellow road sign reading Get Paid to Share against a cloudy sky" style="background:linear-gradient(90deg,#6f9fd6 0%,#c7dbef 55%,#e9d84a 100%)"></div>
    <h3>EVERYBODY BENEFITS<br>FROM REFERRALS</h3>
    <p>We Provide Expert Quality<br>Work for Affordable Price.</p>
  </article>

  <h2 class="abs section-title refer-list"><em>REFER:</em> FLOODS, REMODELS, RENOVATIONS &amp; REPAIRS</h2>

  <div class="abs contact-cta">CALL <span class="hi">TEXT</span> <span class="thin">OR</span> BOOK <span class="hi">ONLINE</span></div>
  <div class="abs contact-line">555-014-2796 | www.TallowRidgeBuilders.example</div>
</section>

</body>
</html>
```